Brivolands Vehicle Wrap Design for Vacation Rental Property Mgt Company

We are looking for a vehicle wrap design to extend our brand through our service vehicles. Design should be simple, professional, eye-catching, and incorporate our logo and corporate colors. Design should be flexible enough to be applied to a wide variety of trucks and cars. Not looking for FULL wrap, but rather separate graphics to be applied to white vehicles. Attached is ppt with a couple of our current vehicles and a few sample designs that has caught our attention. Copies of our current logo and biz card designs are also included.

Panels to include:
Logo (attached)
555-384-9126
www.Brivolands.example
Vacation Rental Property Management
Property Maintenance Services
Linen & Laundry Services

Target Market(s)

Local adults 30-65

Industry/Entity Type

Font styles to use
Serif

Colors
0054AA
0677BA
7BADD7
CADEEF
E8F1F8

Requirements
Must have
• Logo, phone, web address, corporate colors,

```html
<!DOCTYPE html>
<html lang="en">
<head>
<meta charset="utf-8">
<title>Brivolands Vehicle Wrap</title>
<link rel="stylesheet" href="https://fonts.googleapis.com/css2?family=Oswald:wght@500&family=Montserrat:wght@500;600;700&display=swap">
<style>
  :root {
    --white: #ffffff;
    --navy: #0a2a5c;
    --deep: #062354;
    --brand-blue: #0054AA;
    --sky: #1e9ade;
    --mid: #0677BA;
    --soft: #7BADD7;
    --pale: #CADEEF;
    --mist: #E8F1F8;
    --box-1: #6ea7d9;
    --box-2: #4a86c4;
    --box-3: #2b62b0;
  }
  html, body {
    margin: 0;
    padding: 0;
    width: 1200px;
    height: 627px;
    overflow: hidden;
    background: var(--white);
  }
  .wrap-canvas {
    position: relative;
    width: 1200px;
    height: 627px;
    background: var(--white);
    font-family: "Montserrat", sans-serif;
  }
  .wrap-art {
    position: absolute;
    inset: 0;
  }
  .brand-name {
    font-family: "Oswald", sans-serif;
    font-weight: 500;
    font-size: 104px;
    fill: var(--navy);
    letter-spacing: 1px;
  }
  .door-mark {
    position: absolute;
    left: 290px;
    top: 352px;
    display: flex;
    align-items: center;
    gap: 8px;
    font-family: "Oswald", sans-serif;
    font-weight: 500;
    font-size: 24px;
    color: var(--navy);
  }
  .door-mark .mark-square {
    width: 22px;
    height: 22px;
    background: var(--navy);
  }
  .contact-row {
    position: absolute;
    top: 348px;
    left: 655px;
    display: flex;
    align-items: center;
    color: var(--white);
  }
  .contact-phone {
    display: flex;
    align-items: center;
    gap: 8px;
    font-weight: 600;
    font-size: 31px;
    letter-spacing: 0.5px;
  }
  .contact-web {
    display: flex;
    align-items: center;
    gap: 9px;
    margin-left: 30px;
    font-weight: 500;
    font-size: 19px;
    letter-spacing: 1.2px;
  }
  .services {
    position: absolute;
    top: 394px;
    left: 572px;
    display: flex;
  }
  .service {
    height: 55px;
    display: flex;
    align-items: center;
    justify-content: center;
    text-align: center;
    color: var(--white);
    font-weight: 700;
    font-size: 10.5px;
    line-height: 13px;
    text-transform: uppercase;
  }
  .service--rental { width: 116px; background: var(--box-1); }
  .service--maintenance { width: 113px; background: var(--box-2); }
  .service--linen { width: 113px; background: var(--box-3); }
</style>
</head>
<body>
<main class="wrap-canvas">
  <svg class="wrap-art" width="1200" height="627" viewBox="0 0 1200 627" aria-hidden="true">
    <defs>
      <linearGradient id="bandFill" x1="0" y1="0" x2="0" y2="1">
        <stop offset="0" stop-color="var(--sky)"/>
        <stop offset="0.45" stop-color="var(--mid)"/>
        <stop offset="1" stop-color="var(--deep)"/>
      </linearGradient>
    </defs>
    <polygon class="diagonal-band" points="440,506 966,98 1200,98 1200,506" fill="url(#bandFill)"/>
    <polygon class="lower-sliver" points="425,506 480,470 860,470 860,506" fill="var(--deep)"/>
    <text class="brand-name" transform="translate(480 440) rotate(-38)">BRIVOLANDS</text>
  </svg>

  <div class="door-mark">
    <span class="mark-square"></span>
    <span>Brivolands</span>
  </div>

  <div class="contact-row">
    <div class="contact-phone">
      <svg width="24" height="24" viewBox="0 0 24 24" aria-hidden="true">
        <path d="M6.6 10.8a15 15 0 0 0 6.6 6.6l2.2-2.2a1 1 0 0 1 1-.25 11 11 0 0 0 3.6.6 1 1 0 0 1 1 1V20a1 1 0 0 1-1 1A17 17 0 0 1 3 4a1 1 0 0 1 1-1h3.5a1 1 0 0 1 1 1c0 1.25.2 2.45.6 3.6a1 1 0 0 1-.25 1z" fill="none" stroke="var(--white)" stroke-width="1.8"/>
      </svg>
      <span>555-384-9126</span>
    </div>
    <div class="contact-web">
      <svg width="26" height="26" viewBox="0 0 24 24" aria-hidden="true" fill="none" stroke="var(--white)" stroke-width="1.4">
        <circle cx="12" cy="12" r="10"/>
        <ellipse cx="12" cy="12" rx="4.5" ry="10"/>
        <line x1="2" y1="12" x2="22" y2="12"/>
        <line x1="4" y1="7" x2="20" y2="7"/>
        <line x1="4" y1="17" x2="20" y2="17"/>
      </svg>
      <span>brivolands.example</span>
    </div>
  </div>

  <div class="services">
    <div class="service service--rental">Vacation<br>Rental Property<br>Management</div>
    <div class="service service--maintenance">Property<br>Maintenance<br>Services</div>
    <div class="service service--linen">Linen &amp;<br>Laundry<br>Services</div>
  </div>
</main>
</body>
</html>
```